Startup online payment business - Sporting / Golf, Swift Tee payment

Background:
Our business name is "Swift Tee" we provide online payments for golfing services via our website. We currently have a logo used on our website. No other design style has been developed. Our aim is to remove cash payments for service at golf clubs.

Our Key Values:
Quick and easy
Formal and polite
Fun with professional boundary
Mate-ship relationships
100% online digital

What we want from you:
Marketing design to be used on posters and stickers in a retail setting to direct customers to our online payment Chanel.
Design must incorporate attached logo, URL swifttee.com.au and our key values can act as a guide the type of design. We have used color Hex#007672 for logo background. We are open to use other colors.

Target Market(s)

Golf clubs and golf players

Industry/Entity Type

Golf Course

Font styles to use
Sans Serif

Requirements
Must have
• Directions to online payment via URL: swifttee.com.au
Nice to have
• We like the idea of the slogan: No Cash - No worries. Have attached home screen that will be available from URL link. Consideration if using mobile phone in image. Push the online payment and steps 1. Visit swifttee.com 2. Select club 3. Confirm payment
Should not have
• Cartoons

```html
<!DOCTYPE html>
<html lang="en">
<head>
<meta charset="utf-8">
<title>Swift Tee – No Cash No Worries</title>
<link rel="stylesheet" href="https://fonts.googleapis.com/css2?family=Lato:wght@400;700&display=swap">
<style>
  :root {
    --turf-light: #2f7a2f;
    --turf-mid: #266b27;
    --turf-dark: #1f5e22;
    --ink: #ffffff;
  }
  html, body {
    margin: 0;
    padding: 0;
    width: 900px;
    height: 1200px;
    overflow: hidden;
  }
  .poster {
    position: relative;
    width: 900px;
    height: 1200px;
    overflow: hidden;
    font-family: "Lato", sans-serif;
    color: var(--ink);
  }
  .turf-backdrop {
    position: absolute;
    inset: 0;
    background:
      radial-gradient(ellipse at 50% 30%, var(--turf-dark) 0%, transparent 60%),
      linear-gradient(180deg, var(--turf-light) 0%, var(--turf-mid) 45%, var(--turf-dark) 100%);
  }
  .brand-name {
    position: absolute;
    top: 112px;
    left: 0;
    width: 100%;
    margin: 0;
    text-align: center;
    font-weight: 700;
    font-size: 70px;
    letter-spacing: 6px;
    line-height: 1;
  }
  .rule {
    position: absolute;
    left: 132px;
    width: 632px;
    height: 3px;
    background: var(--ink);
  }
  .rule--top { top: 283px; }
  .rule--bottom { top: 681px; }
  .slogan {
    position: absolute;
    top: 385px;
    left: 0;
    width: 100%;
    margin: 0;
    text-align: center;
    font-weight: 700;
    font-size: 101px;
    line-height: 113px;
    letter-spacing: -1px;
  }
  .call-to-action {
    position: absolute;
    top: 763px;
    left: 0;
    width: 100%;
    margin: 0;
    text-align: center;
    font-weight: 400;
    font-size: 41px;
    letter-spacing: 4px;
    line-height: 1;
  }
  .web-address {
    position: absolute;
    top: 927px;
    left: 0;
    width: 100%;
    margin: 0;
    text-align: center;
    font-weight: 400;
    font-size: 53px;
    letter-spacing: 12px;
    padding-left: 12px;
    box-sizing: border-box;
    line-height: 1;
  }
</style>
</head>
<body>
  <main class="poster">
    <div class="turf-backdrop" role="img" aria-label="Close-up photograph of a lush green golf course lawn"></div>
    <p class="brand-name">SWIFT TEE</p>
    <div class="rule rule--top"></div>
    <h1 class="slogan">NO CASH<br>NO WORRIES</h1>
    <div class="rule rule--bottom"></div>
    <p class="call-to-action">PAY YOUR GREEN FEES ONLINE</p>
    <p class="web-address">SWIFTTEE.COM.AU</p>
  </main>
</body>
</html>
```